Australian Web Design company needs a business card design

We need a business card design for a Sydney based Web Design/Development company called "Tall Pine Web Design". We design, build and deploy websites for small to medium sized businesses. The final design should be clean and communicate that we are a professional and supportive company.
I'd like the Icon to be abstract. Something that embodies the power of the internet, needs to be clean/professional and show that we are human and that we support our customers. Hope that helps.
Target Market(s)
All small to medium businesses
Industry/Entity Type
Business
Contact Information for Business Card
Martin Forbes
Tall Pine Web Design
17 Wattle Grove Road
West Kelsworth
NSW 2317
0438 527 064
martin@tallpinewebdesign.com.au
www.tallpinewebdesign.com.au

```html
<!DOCTYPE html>
<html lang="en">
<head>
<meta charset="utf-8">
<title>Tall Pine Web Design – Business Card</title>
<link rel="stylesheet" href="https://fonts.googleapis.com/css2?family=Noto+Sans:wght@400;700&display=swap">
<style>
  :root {
    --page-bg: #ece8e3;
    --wine-light: #b3262a;
    --wine-mid: #7e1a1c;
    --wine-dark: #3a1414;
    --band-light: #d9b8ae;
    --band-fade: #8e4a44;
    --rule: #f4ecea;
    --ink-light: #ffffff;
    --ink-soft: #f3e4e0;
    --ink-dark: #4a4a4c;
  }
  * { box-sizing: border-box; margin: 0; padding: 0; }
  html, body {
    width: 1200px;
    height: 1000px;
    overflow: hidden;
    background: var(--page-bg);
    font-family: "Noto Sans", Verdana, sans-serif;
  }
  .sheet {
    width: 1200px;
    height: 1000px;
    display: flex;
    flex-direction: column;
    align-items: center;
    justify-content: center;
    gap: 60px;
  }
  .card {
    position: relative;
    width: 700px;
    height: 400px;
    overflow: hidden;
    border-radius: 4px;
    box-shadow: 0 10px 28px rgba(40, 20, 20, 0.25);
    background: radial-gradient(ellipse at 45% 40%, var(--wine-light) 0%, var(--wine-mid) 55%, var(--wine-dark) 100%);
  }

  /* Front */
  .front .brand {
    position: absolute;
    left: 26px;
    top: 30px;
    display: flex;
    align-items: center;
    gap: 10px;
  }
  .brand-square {
    width: 22px;
    height: 22px;
    background: var(--ink-light);
  }
  .brand-name {
    font-size: 19px;
    font-weight: 700;
    color: var(--ink-light);
    letter-spacing: 0.3px;
  }
  .front .name-band {
    position: absolute;
    left: 150px;
    right: 0;
    top: 95px;
    height: 150px;
    background: linear-gradient(90deg, var(--band-light) 0%, #c99a90 45%, var(--band-fade) 100%);
    border-bottom: 3px solid var(--rule);
  }
  .front .holder {
    position: absolute;
    left: 36px;
    bottom: 30px;
    font-size: 30px;
    font-weight: 400;
    color: var(--ink-light);
  }
  .front .corner-mark {
    position: absolute;
    right: 34px;
    top: 30px;
    width: 30px;
    height: 30px;
    background: var(--ink-light);
  }
  .front .contact {
    position: absolute;
    right: 30px;
    bottom: 26px;
    text-align: right;
    font-size: 15px;
    font-style: normal;
    line-height: 1.75;
    color: var(--ink-soft);
  }

  /* Back */
  .back .logo-band {
    position: absolute;
    top: 0;
    bottom: 0;
    left: 380px;
    width: 200px;
    background: linear-gradient(180deg, var(--band-light) 0%, #cfa69c 100%);
    display: flex;
    align-items: center;
    justify-content: center;
  }
  .back .brand {
    display: flex;
    align-items: center;
    gap: 10px;
    padding: 0 14px;
  }
  .back .brand-square { background: var(--ink-dark); flex: none; }
  .back .brand-name {
    color: var(--ink-dark);
    font-size: 20px;
    line-height: 1.2;
  }
  .back .website {
    position: absolute;
    left: 30px;
    bottom: 28px;
    font-size: 19px;
    color: var(--ink-soft);
    letter-spacing: 0.5px;
  }
</style>
</head>
<body>
  <main class="sheet">
    <section class="card front" aria-label="Business card front">
      <div class="brand">
        <span class="brand-square"></span>
        <span class="brand-name">Tall Pine Web Design</span>
      </div>
      <div class="corner-mark"></div>
      <div class="name-band">
        <p class="holder">Martin Forbes</p>
      </div>
      <address class="contact">
        0438 527 064<br>
        martin@tallpinewebdesign.com.au<br>
        17 Wattle Grove Road West Kelsworth NSW 2317
      </address>
    </section>

    <section class="card back" aria-label="Business card back">
      <div class="logo-band">
        <div class="brand">
          <span class="brand-square"></span>
          <span class="brand-name">Tall Pine<br>Web Design</span>
        </div>
      </div>
      <p class="website">www.tallpinewebdesign.com.au</p>
    </section>
  </main>
</body>
</html>
```